Financial Services Business Card Design

We are a financial services company Based in London, offering Short term Funding Solutions for companies, raising anywhere between £20,000 and £25million pounds.

The Card must have a professional look as it is going to be handed out to professionals I.E Solicitors, Accountants, Company directors and Business owners.

See Attached our company Logo

Industry/Entity Type

Business

Contact Information for Business Card

Lewis Thorncroft
Suite 41
R K House
Bramblecote Lane
Kingsmere
HP19 4QX

```html
<!DOCTYPE html>
<html lang="en">
<head>
<meta charset="utf-8">
<title>Keystone Bridge Finance – Business Card</title>
<link rel="stylesheet" href="https://fonts.googleapis.com/css2?family=Lato:wght@400;700&display=swap">
<style>
  :root {
    --backdrop: #e9e6e1;
    --card: #ffffff;
    --brand-blue: #1f6fc1;
    --brand-green: #4cc443;
    --ink: #1c1c1c;
    --rule-dark: #2a2a2a;
  }
  * { box-sizing: border-box; margin: 0; padding: 0; }
  html, body { width: 1200px; height: 799px; overflow: hidden; }
  body {
    background: var(--backdrop);
    font-family: "Lato", Arial, sans-serif;
    position: relative;
  }
  .card {
    position: absolute;
    top: 100px;
    width: 360px;
    height: 600px;
    background: var(--card);
    box-shadow: 0 6px 18px rgba(0,0,0,0.18);
    overflow: hidden;
  }
  .card--front { left: 200px; }
  .card--back { left: 640px; }

  .brand {
    position: absolute;
    left: 0; right: 0;
    display: flex;
    align-items: center;
    justify-content: center;
    gap: 10px;
  }
  .card--front .brand { top: 265px; }
  .card--back .brand { top: 100px; }
  .brand__dot {
    width: 18px; height: 18px;
    border-radius: 50%;
    background: var(--brand-green);
  }
  .brand__name {
    font-weight: 700;
    font-size: 25px;
    letter-spacing: 0.5px;
    color: var(--brand-blue);
    text-transform: uppercase;
  }

  .card__art { position: absolute; inset: 0; }

  .contact-name {
    position: absolute;
    left: 98px; top: 272px;
    font-size: 22px;
    letter-spacing: 0.5px;
    color: var(--ink);
    text-transform: uppercase;
    white-space: nowrap;
  }
  .address {
    position: absolute;
    left: 106px; top: 378px;
    list-style: none;
    font-size: 21px;
    line-height: 27px;
    color: var(--ink);
  }
  .address li:not(:first-child) { padding-left: 10px; }
</style>
</head>
<body>

  <section class="card card--front" aria-label="Card front">
    <div class="brand">
      <span class="brand__dot"></span>
      <span class="brand__name">Keystone Bridge</span>
    </div>
  </section>

  <section class="card card--back" aria-label="Card back">
    <svg class="card__art" width="360" height="600" viewBox="0 0 360 600" aria-hidden="true">
      <rect x="0" y="190" width="360" height="14" fill="var(--brand-green)"/>
      <polygon points="60,203 118,203 98,222" fill="var(--brand-green)"/>

      <circle cx="62" cy="292" r="20" fill="var(--brand-green)"/>
      <circle cx="62" cy="285" r="7" fill="#fff"/>
      <path d="M49 303 q13 -14 26 0 z" fill="#fff"/>

      <rect x="60" y="329" width="150" height="4" fill="var(--rule-dark)"/>
      <rect x="215" y="312" width="145" height="4" fill="var(--brand-green)"/>

      <circle cx="66" cy="408" r="20" fill="var(--brand-green)"/>
      <path d="M54 409 l12 -11 l12 11" fill="none" stroke="#fff" stroke-width="3" stroke-linejoin="round"/>
      <rect x="58" y="408" width="16" height="11" fill="none" stroke="#fff" stroke-width="3"/>

      <polygon points="0,520 70,520 90,538 110,520 360,520 360,600 0,600" fill="var(--brand-green)"/>
    </svg>

    <div class="brand">
      <span class="brand__dot"></span>
      <span class="brand__name">Keystone Bridge</span>
    </div>

    <p class="contact-name">Lewis Thorncroft</p>

    <ul class="address">
      <li>Suite 41</li>
      <li>R K House</li>
      <li>Bramblecote Lane</li>
      <li>Kingsmere</li>
      <li>HP19 4QX</li>
    </ul>
  </section>

</body>
</html>
```